Letterhead Design Project

I would like some modern, youthful, yet professional.

Industry/Entity Type

It Professional

Requirements
Must have
• On the left side the names of the Planning Committee:
Planning Committee
Founding Leaders:
Dorvin Pellard, BRIM Youths - Washington, DC
Marisol Trebbett, BRIM Youths - Washington, DC
Corvenna Blaskett, BRIM Youths - Washington, DC
Gregory Pullman, BRIM Youths - Washington, DC
Rhea Tolson, Alliance of Coastal Province Youth In Care Circle
Vesna Korubina, Alliance of Coastal Provnice Youth in Care Circle
Harmony Bolton, United Youth In Care Circle, Canada
Elodie Fern Rivka, United Youth In Care Circle, Canada
Chair
Sheronda Pike, BRIM Youths, Washington, DC
Co-Chairs
Ruth Ellsworth, Worldwide Kinship Home Alliance, Amsterdam. Netherlands
Tessa Broughton, Young Voices Pathways, Jackson, MS
Derek Stowe, Mabel R Thornbury Trust

```html
<!DOCTYPE html>
<html lang="en">
<head>
<meta charset="utf-8">
<title>Planning Committee Letterhead</title>
<link rel="stylesheet" href="https://fonts.googleapis.com/css2?family=Lato:wght@300;400;700&display=swap">
<style>
  :root {
    --navy-deep: #0b2a63;
    --navy: #11408f;
    --blue-bright: #2f6fc4;
    --paper: #ffffff;
    --ink-white: #ffffff;
    --ink-partner: #1d3f7a;
    --dot-partner: #9fb6d9;
  }
  * { margin: 0; padding: 0; box-sizing: border-box; }
  html, body { width: 900px; height: 1200px; overflow: hidden; background: var(--paper); }
  .letterhead {
    position: relative;
    width: 900px;
    height: 1200px;
    background: var(--paper);
    font-family: "Lato", sans-serif;
    overflow: hidden;
  }
  .header-wave { position: absolute; top: 0; left: 0; width: 900px; height: 380px; }
  .committee {
    position: absolute;
    top: 14px;
    color: var(--ink-white);
    font-size: 11.5px;
    line-height: 15.6px;
    font-weight: 300;
    list-style: none;
  }
  .committee--founders { left: 20px; width: 420px; }
  .committee--chairs { left: 444px; width: 440px; }
  .committee .heading { font-weight: 400; }
  .committee .member-name { font-weight: 700; }
  .partner-strip {
    position: absolute;
    left: 0;
    bottom: 20px;
    width: 900px;
    height: 70px;
    display: flex;
    align-items: center;
    justify-content: space-between;
    padding: 0 18px;
  }
  .partner {
    display: flex;
    align-items: center;
    gap: 7px;
    width: 136px;
    color: var(--ink-partner);
    font-size: 11px;
    line-height: 13px;
    font-weight: 400;
  }
  .partner .dot {
    width: 14px;
    height: 14px;
    border-radius: 50%;
    flex: none;
    background: var(--dot-partner);
  }
</style>
</head>
<body>
<div class="letterhead">
  <svg class="header-wave" viewBox="0 0 900 380" aria-hidden="true">
    <defs>
      <radialGradient id="headerFill" cx="0.62" cy="0.55" r="0.75">
        <stop offset="0" stop-color="#3f7fd0"/>
        <stop offset="0.45" stop-color="#17479a"/>
        <stop offset="1" stop-color="#0b2a63"/>
      </radialGradient>
      <linearGradient id="swoosh" x1="0" y1="0" x2="1" y2="0">
        <stop offset="0" stop-color="#2f6fc4" stop-opacity="0"/>
        <stop offset="0.6" stop-color="#5a9ae4" stop-opacity="0.8"/>
        <stop offset="1" stop-color="#2f6fc4" stop-opacity="0.2"/>
      </linearGradient>
    </defs>
    <path d="M0 0 H900 V170 C820 150 720 170 650 220 C560 290 440 330 300 340 C180 348 80 352 0 360 Z" fill="url(#headerFill)"/>
    <path d="M360 320 C500 300 600 240 670 200 C740 162 820 150 900 168 L900 182 C820 168 740 180 680 220 C600 270 490 312 360 320 Z" fill="url(#swoosh)"/>
  </svg>

  <ul class="committee committee--founders">
    <li class="heading">Planning Committee</li>
    <li class="heading">Founding Leaders:</li>
    <li><span class="member-name">Dorvin Pellard</span>, BRIM Youths - Washington, DC</li>
    <li><span class="member-name">Marisol Trebbett</span>, BRIM Youths - Washington, DC</li>
    <li><span class="member-name">Corvenna Blaskett</span>, BRIM Youths - Washington, DC</li>
    <li><span class="member-name">Gregory Pullman</span>, BRIM Youths - Washington, DC</li>
    <li><span class="member-name">Rhea Tolson</span>, Alliance of Coastal Province Youth In Care Circle</li>
    <li><span class="member-name">Vesna Korubina</span>, Alliance of Coastal Provnice Youth in Care Circle</li>
    <li><span class="member-name">Harmony Bolton</span>, United Youth In Care Circle, Canada</li>
    <li><span class="member-name">Elodie Fern Rivka</span>, United Youth In Care Circle, Canada</li>
  </ul>

  <ul class="committee committee--chairs">
    <li class="heading">Chair</li>
    <li><span class="member-name">Sheronda Pike</span>, BRIM Youths, Washington, DC</li>
    <li class="heading">Co-Chairs</li>
    <li><span class="member-name">Ruth Ellsworth</span>, Worldwide Kinship Home Alliance, Amsterdam, Netherlands</li>
    <li><span class="member-name">Tessa Broughton</span>, Young Voices Pathways, Jackson, MS</li>
    <li><span class="member-name">Derek Stowe</span>, Mabel R Thornbury Trust</li>
  </ul>

  <div class="partner-strip">
    <div class="partner"><span class="dot"></span><span>Global Gathering of Youth in Care</span></div>
    <div class="partner"><span class="dot"></span><span>Young Voices Pathways</span></div>
    <div class="partner"><span class="dot"></span><span>Worldwide Kinship Home Alliance</span></div>
    <div class="partner"><span class="dot"></span><span>BRIM Youths</span></div>
    <div class="partner"><span class="dot"></span><span>Halvern Family Fund</span></div>
    <div class="partner"><span class="dot"></span><span>Mabel R Thornbury Trust</span></div>
  </div>
</div>
</body>
</html>
```